International games company requires localisation design of grl prediction game.

Using our current designs and those of our competitors, Lumora Plays are looking for novel design work that refreshes, enlivens and brings our games in line with what is expected in the American market. The Sports lottery game works by users selecting a winning margin for a series of 8 (in this case) GRL games. Should all of these predictions be correct, the user wins the jackpot.We are a software developer that creates free-to-play games specialised for the iGaming industry which function as customer acquisition and retention tools. Our user acquisition and retention models and processes are differentiated from our competitors by being driven by our unique style and application of gamification techniques and user behaviour analysis. Designs submitted should take inspiration from the attached images but designers should feel free to add their own flair and creativity whilst embracing intuitive UX and UI design principles.

Target Market(s)

American Sports fans aged 18+

Font styles to use
Sans Serif

Colors

Designer to choose colors to be used in the design.

Requirements
Must have
• User-friendly, intelligent design, applicable to being recoloured and branded to fit client's brands.

```html
<!DOCTYPE html>
<html lang="en">
<head>
<meta charset="utf-8">
<title>Lumora Plays – GRL Winning Margins</title>
<link rel="stylesheet" href="https://fonts.googleapis.com/css2?family=Open+Sans:wght@400;600;700;800&display=swap">
<style>
:root{
  --status:#000000;
  --banner:#f3c84c;
  --navy:#343466;
  --gold:#ffd21f;
  --green:#27ae60;
  --red:#ef2f3a;
  --bets:#ee2c2c;
  --page:#eeeeee;
  --card:#fbfbfb;
  --line:#d9d9d9;
  --ink:#1c1c1c;
  --muted:#666666;
  --teal:#2a8f8a;
  --margin-red:#d23a32;
  --pick-red:#b8201e;
  --pick-gold:#f1c232;
  --shade:rgba(0,0,0,.48);
}
*{box-sizing:border-box;margin:0;padding:0}
html,body{width:1200px;height:2533px;overflow:hidden}
body{position:relative;background:var(--page);font-family:"Open Sans",Arial,sans-serif;color:var(--ink)}

.status-bar{position:absolute;left:0;top:0;width:1200px;height:98px;background:var(--status)}

.top-bar{position:absolute;left:0;top:98px;width:1200px;height:184px;background:var(--banner)}
.back-btn{position:absolute;left:22px;top:60px;width:84px;height:80px;border:3px solid #222;border-radius:6px}
.back-btn svg{position:absolute;left:22px;top:18px}
.instruction{position:absolute;left:186px;top:34px;font-size:45px;line-height:54px;font-weight:500;color:#111}
.autofill-btn{position:absolute;left:844px;top:58px;width:200px;height:88px;background:var(--green);color:#fff;font-size:40px;font-weight:600;display:flex;align-items:center;justify-content:center;border-radius:4px}
.close-btn{position:absolute;left:1084px;top:58px;width:88px;height:88px;background:var(--red);border-radius:4px}
.close-btn svg{position:absolute;left:20px;top:20px}

.prize-panel{position:absolute;left:0;top:282px;width:1200px;height:465px;background:var(--navy);text-align:center;color:#fff}
.prize-win{position:absolute;left:0;right:0;top:60px;font-size:64px;font-weight:700;letter-spacing:1px}
.prize-amount{position:absolute;left:0;right:0;top:136px;font-size:104px;font-weight:800;color:var(--gold);line-height:1.1}
.prize-rule{position:absolute;left:0;right:0;top:286px;font-size:40px;font-weight:600}
.prize-second{position:absolute;left:0;right:0;top:350px;font-size:40px;font-weight:600;color:var(--gold)}

.fixture{position:absolute;left:22px;width:1149px;height:411px;background:var(--card);border:2px solid var(--line);border-radius:8px;box-shadow:0 4px 8px rgba(0,0,0,.12)}
.fixture-head{position:absolute;left:0;top:0;width:100%;height:244px;border-bottom:2px solid var(--line)}
.team{position:absolute;top:16px;width:180px;text-align:center}
.team.away{left:40px}
.team.home{left:430px}
.helmet{display:block;margin:0 auto;width:130px;height:120px;border-radius:60px 70px 30px 40px}
.team-name{display:block;margin-top:40px;font-size:44px;color:#222}
.at{position:absolute;left:310px;top:84px;font-size:64px;color:#333}
.head-divider{position:absolute;left:710px;top:24px;width:2px;height:196px;background:var(--line)}
.stats-btn,.bets-btn{position:absolute;left:791px;width:248px;height:78px;color:#fff;font-size:38px;display:flex;align-items:center;justify-content:center;border-radius:3px}
.stats-btn{top:22px;background:var(--navy)}
.bets-btn{top:134px;background:var(--bets)}
.margins{position:absolute;left:47px;top:272px;display:flex;gap:12px}
.margin{width:122px;height:72px;border:3px solid var(--margin-red);border-radius:5px;display:flex;align-items:center;justify-content:center;font-size:36px;color:#222;background:#fff}
.margin.away-side{border-color:var(--teal)}
.margin.picked-red{background:var(--pick-red);border-color:var(--pick-red);color:#fff}
.margin.picked-gold{background:var(--pick-gold);border-color:var(--pick-gold);color:#fff}

.shade{position:absolute;left:0;top:747px;width:1200px;height:1786px;background:var(--shade)}

.confirm-dialog{position:absolute;left:100px;top:1033px;width:996px;height:729px;background:#fff;border-radius:8px;text-align:center}
.confirm-title{position:absolute;left:0;right:0;top:52px;font-size:58px;font-weight:700;color:#111}
.celebration{position:absolute;left:408px;top:168px;width:200px;height:200px;background:#111;border-radius:45% 55% 40% 50%}
.confirm-text{position:absolute;left:0;right:0;top:420px;font-size:44px;color:#111}
.ok-btn{position:absolute;left:438px;top:491px;width:146px;height:94px;background:var(--green);color:#fff;font-size:38px;font-weight:700;display:flex;align-items:center;justify-content:center;border-radius:3px}
.edit-link{position:absolute;left:0;right:0;top:634px;font-size:36px;color:var(--muted)}
</style>
</head>
<body>

<div class="status-bar"></div>

<header class="top-bar">
  <div class="back-btn"><svg width="40" height="44" viewBox="0 0 40 44"><path d="M30 4 L10 22 L30 40" fill="none" stroke="#222" stroke-width="4"/></svg></div>
  <div class="instruction">Click the margins<br>to choose your winners</div>
  <div class="autofill-btn">Autofill</div>
  <div class="close-btn"><svg width="48" height="48" viewBox="0 0 48 48"><path d="M6 6 L42 42 M42 6 L6 42" stroke="#fff" stroke-width="5"/></svg></div>
</header>

<section class="prize-panel">
  <div class="prize-win">WIN</div>
  <div class="prize-amount">$ 1,000,000</div>
  <div class="prize-rule">PREDICT 8 WINNING MARGINS</div>
  <div class="prize-second">7 FROM 8 AND WIN $10,000</div>
</section>

<article class="fixture" style="top:789px">
  <div class="fixture-head">
    <div class="team away"><span class="helmet" role="img" aria-label="Norsemen team helmet" style="background:#4b3a8c"></span><span class="team-name">Norsemen</span></div>
    <div class="at">@</div>
    <div class="team home"><span class="helmet" role="img" aria-label="Pilots team helmet" style="background:#cdb37a"></span><span class="team-name">Pilots</span></div>
    <div class="head-divider"></div>
    <div class="stats-btn">Stats</div>
    <div class="bets-btn">Bets</div>
  </div>
  <div class="margins">
    <div class="margin away-side picked-gold">+30</div><div class="margin away-side">24-29</div><div class="margin away-side">1-6</div><div class="margin">1-6</div><div class="margin">7-12</div><div class="margin">13-18</div><div class="margin">24-29</div><div class="margin">30+</div>
  </div>
</article>

<article class="fixture" style="top:1244px">
  <div class="fixture-head">
    <div class="team away"><span class="helmet" role="img" aria-label="Away team helmet" style="background:#2d5aa0"></span><span class="team-name">Rangers</span></div>
    <div class="at">@</div>
    <div class="team home"><span class="helmet" role="img" aria-label="Home team helmet" style="background:#8a8a8a"></span><span class="team-name">Hawks</span></div>
    <div class="head-divider"></div>
    <div class="stats-btn">Stats</div>
    <div class="bets-btn">Bets</div>
  </div>
  <div class="margins">
    <div class="margin away-side">+19</div><div class="margin away-side">13-18</div><div class="margin away-side">1-6</div><div class="margin">1-6</div><div class="margin">7-12</div><div class="margin">13-18</div><div class="margin">19-24</div><div class="margin">30+</div>
  </div>
</article>

<article class="fixture" style="top:1704px">
  <div class="fixture-head">
    <div class="team away"><span class="helmet" role="img" aria-label="Tarpons team helmet" style="background:#1b9aa0"></span><span class="team-name">Tarpons</span></div>
    <div class="at">@</div>
    <div class="team home"><span class="helmet" role="img" aria-label="Barons team helmet" style="background:#e0522a"></span><span class="team-name">Barons</span></div>
    <div class="head-divider"></div>
    <div class="stats-btn">Stats</div>
    <div class="bets-btn">Bets</div>
  </div>
  <div class="margins">
    <div class="margin away-side">+19</div><div class="margin away-side">6-1</div><div class="margin away-side">1-6</div><div class="margin">7-12</div><div class="margin">13-18</div><div class="margin picked-red">19-24</div><div class="margin">24-29</div><div class="margin">30+</div>
  </div>
</article>

<article class="fixture" style="top:2156px">
  <div class="fixture-head">
    <div class="team away"><span class="helmet" role="img" aria-label="Norsemen team helmet" style="background:#4b3a8c"></span><span class="team-name">Norsemen</span></div>
    <div class="at">@</div>
    <div class="team home"><span class="helmet" role="img" aria-label="Pioneers team helmet" style="background:#e8b818"></span><span class="team-name">Pioneers</span></div>
    <div class="head-divider"></div>
    <div class="stats-btn">Stats</div>
    <div class="bets-btn">Bets</div>
  </div>
  <div class="margins">
    <div class="margin away-side">+30</div><div class="margin away-side">29-24</div><div class="margin away-side">24-19</div><div class="margin">7-12</div><div class="margin picked-gold">13-18</div><div class="margin">19-24</div><div class="margin">24-29</div><div class="margin">30+</div>
  </div>
</article>

<div class="shade"></div>

<div class="confirm-dialog" role="dialog">
  <div class="confirm-title">Nice!</div>
  <div class="celebration" role="img" aria-label="Silhouette of a celebrating player"></div>
  <div class="confirm-text">Your entry has been created</div>
  <div class="ok-btn">OK</div>
  <div class="edit-link">Need to edit your picks?</div>
</div>

</body>
</html>
```